Elegant Business Card with Logo and Picture

Please create a business card that has the Logo colors add Gold and turquoise / use the attached logo - I would like a beautiful Business Card - Please make sure it's printed on both sides / Picture can go on one side Logo other
www.velmorshine.example
614-372-0586
Lyn Odessa Ferwick
lynodessaf@quillpost.example
Life Coach
Vantrell Certified Teacher / Life Coach / Interior Designer
Transformational Retreats

Target Market(s)

Women Men General

Industry/Entity Type

Life Coaching

Contact Information for Business Card

www.velmorshine.example
614-372-0586
Lyn Odessa Ferwick
Life Coach
Vantrell Certified Teacher / Yoga Teacher / Interior Designer

Font styles to use
Serif
Decorative

Colors
33a6d6
e34197
ffc214

Requirements
Must have
• Quality Paper and touch /
Nice to have
• Beautiful Touch and feel
Should not have
• needs to be elegant

```html
<!DOCTYPE html>
<html lang="en">
<head>
<meta charset="utf-8">
<title>Velmor Shine Coaching – Business Card</title>
<link href="https://fonts.googleapis.com/css2?family=Lato:wght@400;700&display=swap" rel="stylesheet">
<style>
  :root {
    --stage: #e9e6e2;
    --card-light: #eeeff1;
    --card-dark: #000000;
    --ink: #1a1a1a;
    --white: #ffffff;
    --pink: #e4287f;
    --photo-a: #e9ebee;
    --photo-b: #d9c2ae;
    --photo-c: #c98a7a;
  }
  * { margin: 0; padding: 0; box-sizing: border-box; }
  html, body { width: 1000px; height: 1200px; overflow: hidden; }
  body {
    position: relative;
    background: var(--stage);
    font-family: "Lato", sans-serif;
  }
  .card {
    position: absolute;
    width: 778px;
    height: 446px;
    box-shadow: 0 6px 18px rgba(0,0,0,0.25);
    overflow: hidden;
  }
  .card--front { left: 111px; top: 120px; background: var(--card-light); }
  .card--back  { left: 110px; top: 633px; background: var(--card-dark); }

  .brand {
    position: absolute;
    display: flex;
    align-items: center;
    font-weight: 700;
    text-transform: uppercase;
    white-space: nowrap;
  }
  .brand__dot { border-radius: 50%; background: var(--pink); flex: none; }
  .card--front .brand {
    left: 48px; top: 166px; gap: 10px;
    font-size: 16px; letter-spacing: 1.5px; color: var(--ink);
  }
  .card--front .brand__dot { width: 16px; height: 16px; }
  .card--back .brand {
    left: 0; right: 0; top: 278px; justify-content: center; gap: 14px;
    font-size: 30px; letter-spacing: 3px; color: var(--white);
  }
  .card--back .brand__dot { width: 22px; height: 22px; }

  .contact { position: absolute; left: 48px; top: 230px; color: var(--ink); }
  .contact__name { color: var(--pink); font-weight: 700; font-size: 28px; margin-bottom: 6px; }
  .contact__role { font-size: 18px; line-height: 28px; }
  .contact__list { list-style: none; margin-top: 16px; }
  .contact__item { display: flex; align-items: center; gap: 12px; font-size: 18px; line-height: 28px; }
  .contact__icon { width: 16px; height: 16px; flex: none; }

  .portrait {
    position: absolute; right: 0; top: 0; width: 395px; height: 446px;
    background: linear-gradient(180deg, var(--photo-a) 0%, var(--photo-b) 55%, var(--photo-c) 100%);
  }

  .card__url {
    position: absolute; left: 0; right: 0; top: 387px; text-align: center;
    color: var(--white); font-size: 19px; letter-spacing: 1.5px;
  }
</style>
</head>
<body>

<section class="card card--front">
  <div class="brand"><span class="brand__dot"></span>Velmor Shine Coaching</div>

  <div class="contact">
    <p class="contact__name">Lyn Odessa Ferwick</p>
    <p class="contact__role">Life Coach</p>
    <p class="contact__role">Vantrell Certified Teacher</p>
    <ul class="contact__list">
      <li class="contact__item">
        <svg class="contact__icon" viewBox="0 0 24 24"><path fill="#e4287f" d="M6.6 10.8a15 15 0 0 0 6.6 6.6l2.2-2.2a1 1 0 0 1 1-.25 11.4 11.4 0 0 0 3.6.57 1 1 0 0 1 1 1V20a1 1 0 0 1-1 1A17 17 0 0 1 3 4a1 1 0 0 1 1-1h3.5a1 1 0 0 1 1 1c0 1.25.2 2.45.57 3.6a1 1 0 0 1-.25 1z"/></svg>
        614-372-0586
      </li>
      <li class="contact__item">
        <svg class="contact__icon" viewBox="0 0 24 24"><rect x="2" y="5" width="20" height="14" fill="#e4287f"/><path d="M2 5l10 8 10-8" fill="none" stroke="#eeeff1" stroke-width="1.8"/></svg>
        lynodessaf@quillpost.example
      </li>
      <li class="contact__item">
        <svg class="contact__icon" viewBox="0 0 24 24" fill="none" stroke="#e4287f" stroke-width="2"><circle cx="12" cy="12" r="10"/><ellipse cx="12" cy="12" rx="4.5" ry="10"/><path d="M2 12h20M4 7h16M4 17h16"/></svg>
        www.velmorshine.example
      </li>
    </ul>
  </div>

  <div class="portrait" role="img" aria-label="Portrait photograph of the coach in a patterned off-shoulder top against a light wall"></div>
</section>

<section class="card card--back">
  <div class="brand"><span class="brand__dot"></span>Velmor Shine Coaching</div>
  <p class="card__url">www.velmorshine.example</p>
</section>

</body>
</html>
```